Pillow Company needs Pillow Insert Design

I just started a new pillow line with two pillow types. I have a hotel pillow and an organic pillow. I need two pillow insert signs designed that follow the same layout but are different color types. I want one sign to incorporate silver and white look and another sign to incorporate a green and white look (this one to look organic). They must have the same layout but different colors. I have include examples of what I want it to look like. In addition, I have uploaded the two hi res images for each sign. My logo is uploaded too.

I am open to other concepts and colors as long as it looks modern, clean and upscale. In addition, I need a Made in the USA logo on the pillow insert designs.

I have attached details on sign, images to be used, and examples that I like.

The Pillow Sign Size is 12 inches x 12 inches.

```html
<!DOCTYPE html>
<html lang="en">
<head>
<meta charset="utf-8">
<title>LunaRest Alternative Down Pillow Insert</title>
<link rel="stylesheet" href="https://fonts.googleapis.com/css2?family=Jost:wght@600;700&family=Caladea:wght@400;700&family=Arimo:wght@400;700&display=swap">
<style>
  :root {
    --backdrop: #3fe21f;
    --leaf: #6cf515;
    --leaf-deep: #5fdc12;
    --leaf-text: #56d40e;
    --paper: #ffffff;
    --ink-white: #ffffff;
    --shadow: rgba(0, 60, 0, 0.35);
  }
  * { margin: 0; padding: 0; box-sizing: border-box; }
  html, body { width: 1200px; height: 1000px; overflow: hidden; }
  body { background: var(--backdrop); position: relative; }

  .insert {
    position: absolute; left: 150px; top: 50px; width: 900px; height: 900px;
    background: var(--leaf);
    box-shadow: 4px 6px 14px var(--shadow);
  }
  .insert__frame {
    position: absolute; inset: 12px;
    border: 1.5px solid var(--ink-white);
  }
  .insert__frame--inner { inset: 18px; border-width: 1px; }

  .brand {
    position: absolute; left: 75px; top: 52px; width: 372px; height: 103px;
    background: var(--paper);
    display: flex; align-items: center; justify-content: center; gap: 16px;
  }
  .brand__mark { width: 46px; height: 46px; background: var(--leaf-deep); }
  .brand__name {
    font-family: "Jost", sans-serif; font-weight: 700; font-size: 46px;
    color: var(--leaf-deep); letter-spacing: 0.5px;
  }

  .intro {
    position: absolute; left: 472px; top: 53px; width: 353px;
    font-family: "Caladea", serif; font-size: 13.6px; line-height: 17.4px;
    color: var(--ink-white); text-align: justify; letter-spacing: 0.4px;
  }

  .title {
    position: absolute; left: 75px; top: 168px;
    font-family: "Jost", sans-serif; font-weight: 700; font-size: 54px;
    color: var(--ink-white); letter-spacing: 0.3px; line-height: 1;
  }
  .tagline {
    position: absolute; left: 76px; top: 237px;
    font-family: "Caladea", serif; font-weight: 700; font-size: 18.5px;
    line-height: 24px; color: var(--ink-white);
  }

  .feature-band {
    position: absolute; left: 0; top: 300px; width: 900px; height: 486px;
    background: var(--paper);
  }
  .feature-band__photo {
    position: absolute; left: 383px; top: 0; width: 517px; height: 330px;
    background: linear-gradient(180deg, #d9dedb 0%, #eceeec 45%, #f6f6f4 75%, #ffffff 100%);
  }

  .features {
    position: absolute; left: 68px; top: 24px; list-style: none;
    font-family: "Arimo", sans-serif; font-size: 19px; line-height: 23.2px;
    color: var(--leaf-text);
  }
  .features li { position: relative; padding-left: 37px; width: 330px; }
  .features li::before {
    content: "❖"; position: absolute; left: 0; top: 0; font-size: 15px;
  }
  .features b { font-weight: 700; }

  .slogan {
    position: absolute; left: 74px; top: 423px; width: 547px; height: 45px;
    border: 2px solid var(--leaf-deep);
    font-family: "Caladea", serif; font-weight: 700; font-size: 32px;
    color: var(--leaf-deep); text-align: center; line-height: 40px;
  }

  .origin-badge {
    position: absolute; left: 679px; top: 733px; width: 135px; height: 98px;
    background: var(--paper); padding: 6px;
    box-shadow: 0 1px 3px rgba(0,0,0,0.25);
  }
  .origin-badge__fill {
    width: 100%; height: 62px;
    background: linear-gradient(180deg, #b8263a 0%, #c94a5a 50%, #d7d7e6 100%);
  }
  .origin-badge__base { margin-top: 8px; height: 10px; background: #2b2b45; }

  .craft-note {
    position: absolute; left: 90px; top: 806px;
    font-family: "Caladea", serif; font-weight: 700; font-size: 27px;
    color: var(--ink-white);
  }
</style>
</head>
<body>
  <main class="insert">
    <div class="insert__frame"></div>
    <div class="insert__frame insert__frame--inner"></div>

    <div class="brand">
      <span class="brand__mark"></span>
      <span class="brand__name">LunaRest</span>
    </div>

    <p class="intro">We added revolutionary features from our advanced Super Soft Premium Memory Foam that has an open cell structure design that recovers quickly and does not trap heat to our gel infused polyester fiber to our 100% Certified Organic Cotton Fabric.</p>

    <h1 class="title">Alternative Down Pillow</h1>
    <p class="tagline">This pillow was designed to give you the most comfortable night's sleep in your life.<br>Designed for all types of sleep positions.</p>

    <section class="feature-band">
      <div class="feature-band__photo" role="img" aria-label="Photo of a couple resting together in a bright bed with white linens"></div>
      <ul class="features">
        <li>Made From the Finest Premium Materials</li>
        <li>Adjusts to your Body Weight and Temperature</li>
        <li>100% Certified Organic Cotton Fabric</li>
        <li>Cool Non-Allergenic, Anti-Microbial, and Hypoallergenic</li>
        <li>Conforms to <b>H</b>ead and <b>N</b>eck for optimal <b>A</b>lignment during <b>S</b>leep</li>
        <li>Mildew Proof and Dust Mite Resistant</li>
        <li>PureCell ® toxin free certified foam</li>
      </ul>
      <div class="slogan">Surround Yourself with the Best!</div>
    </section>

    <div class="origin-badge" role="img" aria-label="Made in the USA flag badge">
      <div class="origin-badge__fill"></div>
      <div class="origin-badge__base"></div>
    </div>

    <p class="craft-note">Individually Handcrafted</p>
  </main>
</body>
</html>
```